Palvette International needs a book cover

I am self publishing a book titles entitled, Quiet Threads Through Carrying and Raising. Pressline Yard is ready to do the print, but I did not like their design. I am attaching the picture I want on the front.

Hello all - Thank you all for your beautiful designs.  I am closing this project in 24 hours. I will be making my final selection then.  I apologize for closing earlier than my deadline.  This is my first project and I have learned a lot:)  I will be back with more projects!

```html
<!DOCTYPE html>
<html lang="en">
<head>
<meta charset="utf-8">
<title>Quiet Threads Through Carrying and Raising — Back Cover</title>
<link rel="stylesheet" href="https://fonts.googleapis.com/css2?family=Cinzel:wght@400;700&family=Cormorant+Garamond:ital,wght@1,500&display=swap">
<style>
  :root {
    --ink: #1b1a26;
    --blush: #f3c6de;
    --rose: #eaa9cc;
    --petal: #fbe8f2;
    --lavender: #c9b8e6;
    --mist: #fdf7fb;
    --portrait: #7e9393;
  }
  html, body {
    margin: 0;
    padding: 0;
    overflow: hidden;
    background: #ffffff;
  }
  .cover {
    position: relative;
    width: 729px;
    height: 1200px;
    overflow: hidden;
    background: var(--mist);
  }
  .cover-art {
    position: absolute;
    inset: 0;
    background:
      radial-gradient(ellipse 46% 24% at 28% 4%, var(--rose) 0%, rgba(234,169,204,0) 100%),
      radial-gradient(ellipse 55% 35% at 12% 28%, var(--blush) 0%, rgba(243,198,222,0) 100%),
      radial-gradient(ellipse 60% 32% at 20% 74%, var(--lavender) 0%, rgba(201,184,230,0) 100%),
      radial-gradient(ellipse 40% 25% at 85% 60%, var(--petal) 0%, rgba(251,232,242,0) 100%),
      radial-gradient(ellipse 70% 50% at 55% 45%, #ffffff 0%, rgba(255,255,255,0) 100%),
      linear-gradient(170deg, var(--petal) 0%, var(--mist) 45%, #f4e6f4 70%, var(--blush) 100%);
  }
  .quote {
    position: absolute;
    left: 105px;
    top: 222px;
    width: 600px;
    margin: 0;
    color: var(--ink);
    font-family: "Cinzel", serif;
    font-weight: 400;
    font-size: 34px;
    line-height: 38px;
    letter-spacing: 0.5px;
    text-transform: uppercase;
  }
  .quote-line { display: block; white-space: nowrap; }
  .quote-emphasis {
    display: block;
    text-align: right;
    padding-right: 30px;
    margin-top: -4px;
    font-family: "Cormorant Garamond", serif;
    font-style: italic;
    font-weight: 500;
    font-size: 66px;
    line-height: 58px;
    text-transform: none;
    letter-spacing: 0;
  }
  .quote-mark {
    position: absolute;
    font-family: "Cormorant Garamond", serif;
    font-style: italic;
    font-size: 96px;
    line-height: 1;
    color: var(--ink);
  }
  .quote-mark.open { left: 46px; top: 196px; }
  .quote-mark.close { left: 690px; top: 212px; }
  .author-portrait {
    position: absolute;
    left: 48px;
    top: 830px;
    width: 242px;
    height: 244px;
    background: var(--portrait);
    box-shadow: 0 0 12px 6px var(--portrait);
    border-radius: 4px;
  }
  .author-bio {
    position: absolute;
    left: 329px;
    top: 818px;
    width: 390px;
    margin: 0;
    color: var(--ink);
    font-family: "Cinzel", serif;
    font-size: 22px;
    line-height: 32px;
    text-transform: uppercase;
  }
  .author-name { font-weight: 700; }
</style>
</head>
<body>
  <main class="cover">
    <div class="cover-art" role="img" aria-label="Soft-focus photograph of a mother resting with a crown of small pink flowers, in pale pink and lavender tones"></div>

    <span class="quote-mark open" aria-hidden="true">“</span>
    <blockquote class="quote">
      <span class="quote-line">Mothers are the spiritual</span>
      <span class="quote-line">glue that holds a family</span>
      <span class="quote-emphasis">together.</span>
    </blockquote>
    <span class="quote-mark close" aria-hidden="true">”</span>

    <div class="author-portrait" role="img" aria-label="Author portrait photograph"></div>
    <p class="author-bio">
      <span class="author-name">Lorna Palvette</span><br>
      is the proud mother<br>
      of three amazing,<br>
      beautiful children,<br>
      Tessa, Milo and Greta.<br>
      She is a passionate<br>
      educator, engineer,<br>
      and writer.
    </p>
  </main>
</body>
</html>
```